B2B EDM Banner Design- Specialist Tech Company

We need a new top-of-email banner for our EDM campaigns for Varnel Brix (www.varnelbrix-example.com
). This banner will sit at the top of every email and must immediately signal the brand, look modern and professional, and be visually aligned with the tech/IT audience.
Size of the banner: Around 728x90 - it must fit at the top of an email blast.
Purpose of the Banner
Establish a strong, recognizable brand identity across all Varnel Brix EDMs
visually consistent with existing banners created for other brands (see reference examples provided)
Communicate Varnel Brix’s value proposition at a glance
Brand Name
Varnel Brix
Tagline (must appear in the banner)
“11,322 whitepapers from 726 companies”
Design Requirements
Style & Tone
Modern, clean, and professional
Tech-centric look and feel
High-quality, sleek, and corporate
Eye-catching but not cluttered
Should feel premium and authoritative
Layout & Composition
Full-width banner for email header
Horizontal orientation similar to the Plomtar and Quindle Staff Archive examples
Include space for the brand name/logo prominently on the left or centered
Integrate the tagline in a readable, secondary position
Optional: a subtle background texture or tech-related abstract pattern (circuitry, network nodes, gradient, etc.)
No busy imagery—should feel clean and trustworthy
Color Palette
Use colors consistent with Varnel Brix branding from www.varnelbrix-example.com
Blues, greys, blacks, and tech-style gradients preferred
Should feel consistent with a B2B IT audience
Typography
Clean, sans-serif fonts (professional/tech-aligned)
Brand name should be bold and prominent
Tagline should be smaller, but still readable on desktop and mobile
Imagery (if used)
Abstract tech shapes, network visuals, geometric patterns, or gradient overlays
Avoid photography of people
Keep imagery subtle so text remains legible
Call-to-Action Button (optional)
None required in this banner (unlike the HR examples)
Banner should remain a pure brand header
Deliverables
Final banner in PNG and JPG formats
2–3 design variations (if possible) for A/B testing
Dimensions optimized for EDM: ~600–700px wide (standard email width), proportionate height

```html
<!DOCTYPE html>
<html lang="en">
<head>
<meta charset="utf-8">
<title>Varnel Brix – Email Header Banner</title>
<link href="https://fonts.googleapis.com/css2?family=Roboto:wght@500;700;900&display=swap" rel="stylesheet">
<style>
  :root {
    --bg-left: #0b45b8;
    --bg-mid: #123a86;
    --bg-right: #1c2f4e;
    --glow: rgba(60, 140, 255, 0.35);
    --text: #ffffff;
    --accent: #3fa9f5;
  }
  * { margin: 0; padding: 0; box-sizing: border-box; }
  html, body {
    width: 1200px;
    height: 150px;
    overflow: hidden;
    background: var(--bg-right);
  }
  .banner {
    position: relative;
    width: 1200px;
    height: 150px;
    overflow: hidden;
    font-family: "Roboto", Arial, sans-serif;
    color: var(--text);
  }
  .banner__backdrop {
    position: absolute;
    inset: 0;
    background:
      radial-gradient(ellipse 420px 220px at 90px 40px, var(--glow), transparent 70%),
      linear-gradient(90deg, var(--bg-left) 0%, var(--bg-mid) 40%, var(--bg-right) 100%);
  }
  .brand {
    position: absolute;
    left: 51px;
    top: 40px;
    height: 70px;
    display: flex;
    align-items: center;
    gap: 20px;
  }
  .brand__mark {
    width: 70px;
    height: 70px;
    border-radius: 50%;
    background: var(--accent);
    flex-shrink: 0;
  }
  .brand__name {
    font-size: 34px;
    font-weight: 900;
    letter-spacing: 0.5px;
    text-transform: uppercase;
    line-height: 1;
    color: var(--text);
  }
  .tagline {
    position: absolute;
    left: 451px;
    top: 50%;
    transform: translateY(-50%);
    font-size: 40px;
    font-weight: 700;
    line-height: 1;
    white-space: nowrap;
    color: var(--text);
  }
</style>
</head>
<body>
  <header class="banner">
    <div class="banner__backdrop" role="img" aria-label="Abstract network of nodes and lines over a faint world map in deep blue tones"></div>
    <div class="brand">
      <span class="brand__mark" aria-hidden="true"></span>
      <span class="brand__name">Varnel Brix</span>
    </div>
    <p class="tagline">11322 Whitepapers from 726 Companies</p>
  </header>
</body>
</html>
```